Steel Company / Iron Railing Business Card Template

We are a custom steel fabrication company located in Trainer, PA. In business since 1979, we recently developed a new logo, and we're looking for a business card design to help display the new logo and our business. The name of the company is Kelbrook Forge Co.. The Office Phone number is (610) 555-0143. We fabricate and install custom "wrought iron" railings on our residential side, we also fabricate and erect structural steel (think cranes and steel beams in buildings) on our commercial side. Looking to get a business card template designed. Something modern, but professional. Clear and easy to read. Front should have all business and employee information including phone number(s), email address, business information, etc. back should spotlight logo.

Industry/Entity Type

Construction / Home Improvement

Contact Information for Business Card

Business information is Kelbrook Forge Co., 48 Dunmore Ave Suite 3305, Trainer, PA 19074. Phone number is (610) 555-0143. Website is www.kelbrookforge.example Business card should be for "Tom Pelling" with the job title "Sales & Estimating" but be editable for other employees. Tom's phone number is (610) 555-0178

Colors

Designer to choose colors to be used in the design.

Requirements
Must have
• Modern Feel, Design should be sized for standard business card sizing 3.5" x 2" (88.9mm x 50.8mm)

```html
<!DOCTYPE html>
<html lang="en">
<head>
<meta charset="utf-8">
<title>Kelbrook Forge Co. Business Card</title>
<link href="https://fonts.googleapis.com/css2?family=Montserrat:wght@300;400;500;700;800&display=swap" rel="stylesheet">
<style>
  :root {
    --stage: #9b9b9b;
    --navy: #233f8f;
    --red: #d2232a;
    --grey-text: #7d7d7d;
    --faint: #e2e2e2;
    --white: #ffffff;
    --steel-light: #c9ced3;
    --steel-mid: #a9afb5;
    --steel-dark: #8e959c;
  }
  * { margin: 0; padding: 0; box-sizing: border-box; }
  html, body {
    width: 1200px; height: 1000px; overflow: hidden;
    background: var(--stage);
    font-family: "Montserrat", sans-serif;
  }
  .card {
    position: absolute;
    left: 329px;
    width: 543px; height: 313px;
    border-radius: 24px;
    overflow: hidden;
  }
  /* Back: logo spotlight */
  .card--back { top: 187px; }
  .steel-surface {
    position: absolute; inset: 0;
    background: radial-gradient(ellipse at 45% 40%, var(--steel-light), var(--steel-mid) 60%, var(--steel-dark));
  }
  .back-brand {
    position: absolute; left: 0; right: 0; top: 118px;
    text-align: center;
    font-weight: 800; font-size: 36px; color: var(--navy);
    letter-spacing: -0.5px;
  }
  .back-url {
    position: absolute; left: 0; right: 0; top: 270px;
    text-align: center;
    font-weight: 400; font-size: 17px; color: var(--navy);
  }
  .back-url b { font-weight: 800; }

  /* Front: contact details */
  .card--front { top: 539px; background: var(--white); }
  .contact {
    position: absolute; left: 20px; width: 208px; top: 42px;
    text-align: center;
  }
  .brand {
    display: flex; align-items: center; justify-content: center; gap: 6px;
    height: 40px;
    font-weight: 800; font-size: 15px; color: var(--navy);
  }
  .brand-dot { width: 12px; height: 12px; border-radius: 50%; background: var(--red); }
  .person-name {
    margin-top: 40px;
    font-weight: 700; font-size: 16px; color: var(--navy); letter-spacing: 0.2px;
  }
  .person-title { font-weight: 400; font-size: 16px; color: var(--red); line-height: 1.2; }
  .icons { display: flex; justify-content: center; gap: 4px; margin-top: 7px; }
  .icons svg { width: 25px; height: 25px; }
  .details { margin-top: 6px; font-size: 13px; color: var(--grey-text); line-height: 18px; }
  .divider { width: 64px; height: 1.5px; background: var(--red); margin: 6px auto 0; }
  .address {
    margin-top: 11px; font-size: 9.5px; font-weight: 300; color: var(--grey-text);
    white-space: nowrap; margin-left: -20px; margin-right: -20px;
  }
  .faint-brand {
    position: absolute; left: 245px; top: 55px;
    font-weight: 800; font-size: 66px; line-height: 0.95; color: var(--faint);
    white-space: nowrap;
  }
</style>
</head>
<body>
  <section class="card card--back">
    <div class="steel-surface" role="img" aria-label="Brushed, scratched steel plate texture"></div>
    <div class="back-brand">Kelbrook Forge Co.</div>
    <div class="back-url">www.<b>kelbrookforge</b>.example</div>
  </section>

  <section class="card card--front">
    <div class="faint-brand" aria-hidden="true">Kelbrook<br>Forge Co.</div>
    <div class="contact">
      <div class="brand"><span class="brand-dot"></span>Kelbrook Forge Co.</div>
      <div class="person-name">TOM PELLING</div>
      <div class="person-title">Sales &amp; Estimating</div>
      <div class="icons">
        <svg viewBox="0 0 24 24" aria-label="Phone"><circle cx="12" cy="12" r="12" fill="var(--navy)"/><path d="M9 6.5l2 2.5-1.2 1.4c.7 1.6 2 2.9 3.6 3.6l1.4-1.2 2.5 2-1 1.9c-4.6-.3-8.6-4.3-8.9-8.9z" fill="#fff"/></svg>
        <svg viewBox="0 0 24 24" aria-label="Email"><circle cx="12" cy="12" r="12" fill="var(--navy)"/><rect x="6" y="8" width="12" height="8.5" fill="none" stroke="#fff" stroke-width="1.3"/><path d="M6 8l6 5 6-5M6 16.5l4.5-4.5M18 16.5l-4.5-4.5" fill="none" stroke="#fff" stroke-width="1.2"/></svg>
        <svg viewBox="0 0 24 24" aria-label="Website"><circle cx="12" cy="12" r="12" fill="var(--navy)"/><g fill="none" stroke="#fff" stroke-width="1.1"><circle cx="12" cy="12" r="6"/><ellipse cx="12" cy="12" rx="2.6" ry="6"/><path d="M6 12h12M7 9h10M7 15h10"/></g></svg>
      </div>
      <div class="details">
        (610) 555-0178<br>
        info@kelbrookforge.example<br>
        kelbrookforge.example
      </div>
      <div class="divider"></div>
      <div class="address">48 Dunmore Ave, Suite 3305, Trainer, PA 19074</div>
    </div>
  </section>
</body>
</html>
```